Webdesign für Restaurant / Elif Grillstube
Zielgruppe
Wir führen ein türkisches Restaurant/Imbiss mit einem Catering Service und Lieferservice. Unser Betrieb ist ein 'zwischen Ding'.
Sie können es sich wie ein türkisches 'Morgenpost' oder 'Bistro Lunara' vorstellen.
Wir haben Sitzplätze und Laufkundschaft.
Zielgruppe:
Jeder der gerne gutes Essen isst.
Aufgabenstellung
Unsere Webseite soll ein "Onepager" werden.
Sie sollte auch für mobil Geräte optimiert sein.
Die Internetseite soll bei dem Interessenten folgenden Eindruck hinterlassen: Dass wir wissen was wir machen, dass wir professionell arbeiten und dass sie bei uns qualitativ hochwertiges Essen bekommen.
Die folgende Seite gefällt mir sehr gut:
http://www.vomo-bistro.com
Die Funktionsweise (Auf die Menüpunkte drücken und runterscrollen) soll die gleiche, wie auf dieser Seite sein.
Was mich an dieser Seite stört:
Die Startseite(ganz oben) wirkt meiner Meinung nach etwas "lasch". Sie wirkt etwas zu grau, leblos. Zu dunkel gehalten.
Sie sollten sich trotzdem an der erwähnten Seite orientieren, da mir der Aufbau und die sonstige Gestaltung sehr gut gefällt.
Sie können sich auch an dieser Seite orientieren:
https://www.zahlwerk.com
Farben: keine konkrete Vorstellung. Sollte sich jedoch nicht mit unserem Logo beißen.
Bilder: Sie haben freie Wahl. Wenn Sie Bilder von Speisen verwenden, sollten Sie sich an
unserer Speisekarte orientieren.
Ich sende ihnen Bilder zu, die Sie nutzen können. Müssen Sie aber nicht.
Bilder sind gekauft oder selbst gemacht.
Aufbau und Elemente zu den jeweiligen Abschnitten:
- Home: Catering sollte etwas hervorgehoben werden
Unsere Telefonnummer sollte leicht zu finden sein.
Beispiel: https://www.fjordhase.de/de/
Hintergrundbild: Ansprechendes Foto von einem Gericht(Essen)
- Anschrift
- Öffnungszeiten
- Link zu unserer Facebookseite
- (Impressum hier enthalten)
- Catering
- Lieferservice
- Menu: Unsere Speisen sollten hier übersichtlich auftauchen. (Unsere Karte finden sie auf
- Getränke: Unsere Getränke sollten hier übersichtlich auftauchen
Texte zu den Menüpunkten: <..

```html
<!DOCTYPE html>
<html lang="de">
<head>
<meta charset="utf-8">
<title>Elif Grillstube – Onepager Webdesign</title>
<link href="https://fonts.googleapis.com/css2?family=Archivo:wght@400;500;700;800;900&display=swap" rel="stylesheet">
<style>
:root{
  --green:#1d7a3c;
  --green-dark:#145a2b;
  --ink:#1f1f1f;
  --muted:#555;
  --paper:#ffffff;
  --stage:#eef0ee;
  --line:#d8dbd8;
}
*{box-sizing:border-box;margin:0;padding:0}
html,body{width:1200px;height:2184px;overflow:hidden}
body{background:var(--stage);font-family:"Archivo",Arial,sans-serif;color:var(--ink);position:relative}
.row{position:absolute;left:0;width:1200px;height:421px}
.screen{position:absolute;background:var(--paper);overflow:hidden;box-shadow:0 0 0 1px var(--line)}
.desk{left:60px;top:0;width:600px;height:338px}
.tab{left:700px;top:8px;width:270px;height:322px}
.mob{left:1010px;top:100px;width:150px;height:240px}

/* sidebar */
.sidebar{position:absolute;left:0;top:0;bottom:0;background:var(--paper);text-align:center}
.desk .sidebar{width:96px}
.tab .sidebar{width:78px}
.brand{display:flex;flex-direction:column;align-items:center;gap:4px;margin-top:16px}
.brand-dot{width:14px;height:14px;border-radius:50%;background:var(--green)}
.brand-name{color:var(--green);font-weight:800;font-size:10px;line-height:1.1;width:70px}
.tab .brand-name{font-size:9px}
.nav{list-style:none;margin-top:26px;display:flex;flex-direction:column;align-items:center;gap:12px}
.tab .nav{gap:10px;margin-top:22px}
.nav li{font-size:7px;font-weight:800;letter-spacing:.3px}
.tab .nav li{font-size:6px}
.nav .is-active{border:1px solid var(--ink);padding:1px 4px}
.contact{position:absolute;left:12px;bottom:54px;display:flex;gap:5px;text-align:left}
.tab .contact{left:6px}
.contact svg{width:12px;height:12px;flex:none;margin-top:1px}
.contact p{font-size:6.5px;line-height:1.25;color:var(--muted)}
.contact .nums{margin-top:5px}
.social{position:absolute;left:30px;bottom:18px;display:flex;gap:10px;align-items:center}
.tab .social{left:22px}
.social .circle{width:12px;height:12px;border-radius:50%;background:var(--ink)}
.social svg{width:14px;height:10px}

/* right rail */
.rail{position:absolute;right:0;top:0;bottom:0;width:22px}
.rail .label{position:absolute;top:12px;left:7px;writing-mode:vertical-rl;font-size:7px;color:var(--muted)}
.rail .scroll{position:absolute;bottom:16px;left:7px;writing-mode:vertical-rl;font-size:7px;color:var(--muted)}
.rail .arrow{position:absolute;bottom:6px;left:8px;width:0;height:0;border-left:3px solid transparent;border-right:3px solid transparent;border-top:5px solid var(--ink)}
.dots{position:absolute;top:150px;left:9px;display:flex;flex-direction:column;gap:11px}
.dots i{width:3px;height:3px;border-radius:50%;background:var(--ink);display:block}

/* photos */
.photo{position:absolute}
.ph-pide{background:radial-gradient(ellipse at 45% 55%,#c2481f 0%,#9b3a1b 35%,#6b4a33 65%,#8a6a4d 100%)}
.ph-interior{background:linear-gradient(180deg,#cfd3d2 0%,#9aa19f 40%,#3b3a36 75%,#5f6b60 100%)}
.ph-kebab{background:radial-gradient(circle at 55% 60%,#8a5630 0%,#5c3520 40%,#2e1e14 80%),#2e1e14}
.ph-baklava{background:radial-gradient(circle at 45% 50%,#c99343 0%,#8e6a3d 30%,#2c3550 60%,#1f2638 100%)}
.ph-terrace{background:linear-gradient(180deg,#e9ecea 0%,#b8bdbb 35%,#5a5e5e 65%,#7b8080 100%)}

.hero-title{position:absolute;color:#fff;font-weight:900;line-height:1.08}
.underline{display:block;width:28px;height:2px;background:var(--green);margin:8px 0}
.center .underline{margin:8px auto}
h2.sect{font-weight:900;line-height:1.05;color:var(--ink)}
h2.sect em{font-style:normal;color:var(--green)}
.body{font-size:7px;line-height:1.3;color:var(--muted);text-align:justify}
.body p+p{margin-top:7px}
.body strong{color:var(--ink)}
.btn{display:inline-block;border:1px solid var(--green);color:var(--green);font-size:10px;letter-spacing:.5px;padding:3px 14px}
.map{background:linear-gradient(135deg,#e6e8e4,#d6dbd2 60%,#cfe3c9)}

/* mobile */
.mob-head{position:absolute;top:0;left:0;right:0;height:40px;display:flex;align-items:center;justify-content:center}
.mob-head .brand{margin:0;gap:2px}
.mob-head .brand-dot{width:10px;height:10px}
.mob-head .brand-name{font-size:7px;width:60px}
.burger{position:absolute;right:8px;top:8px;width:9px;display:flex;flex-direction:column;gap:1.5px}
.burger i{display:block;height:1px;background:var(--ink)}
.mob-label{position:absolute;top:42px;left:6px;font-size:4px;color:var(--muted)}
.mob .photo{left:6px;right:6px}
.mob .hero-title{font-size:11px;left:10px}
.mob-foot{position:absolute;left:0;right:0;bottom:0;height:18px;border-top:1px solid var(--line);display:flex;align-items:center;gap:4px;padding:0 6px;font-size:3.6px;color:var(--muted);line-height:1.2}
.mob-foot svg{width:7px;height:7px}
.mob-foot .sp{flex:1}
.mob-foot .circle{width:6px;height:6px;border-radius:50%;background:var(--ink)}
.mob .body{font-size:3.6px}
</style>
</head>
<body>

<!-- shared icon symbols -->
<svg width="0" height="0" style="position:absolute">
  <symbol id="ico-phone" viewBox="0 0 24 24"><path d="M5 2l4 1 1 5-2.5 1.5a12 12 0 0 0 7 7L16 14l5 1 1 4-3 3C10 21 3 14 2 5z" fill="#1f1f1f"/></symbol>
  <symbol id="ico-mail" viewBox="0 0 28 20"><rect x="1" y="1" width="26" height="18" fill="none" stroke="#1f1f1f" stroke-width="2"/><path d="M1 1l13 10L27 1" fill="none" stroke="#1f1f1f" stroke-width="2"/></symbol>
</svg>

<!-- ============ HOME ============ -->
<section class="row" style="top:30px">
  <div class="screen desk">
    <aside class="sidebar">
      <div class="brand"><span class="brand-dot"></span><span class="brand-name">Elif Grillstube</span></div>
      <ul class="nav"><li>HOME</li><li>ELIF GRILLSTUBE</li><li class="is-active">CATERING</li><li>LIEFERSERVICE</li><li>MENU</li></ul>
      <div class="contact"><svg><use href="#ico-phone"/></svg><p>Lieferservice &amp;<br>Catering:<span class="nums" style="display:block">02302 48120<br>01577 9921365</span></p></div>
      <div class="social"><span class="circle"></span><svg><use href="#ico-mail"/></svg></div>
    </aside>
    <div class="photo ph-pide" role="img" aria-label="Foto: Pide mit Peperoni und Gewürzen auf Holzbrett" style="left:96px;top:10px;width:480px;height:318px"></div>
    <h1 class="hero-title" style="left:128px;top:80px;font-size:22px">Geschmack &amp;<br>Qualität in Tradition.<span class="underline"></span>Über 20 Jahre.</h1>
    <div class="rail"><span class="label">home</span><div class="dots"><i></i><i></i><i></i><i></i></div><span class="scroll">scroll down</span><span class="arrow"></span></div>
  </div>
  <div class="screen tab">
    <aside class="sidebar">
      <div class="brand"><span class="brand-dot"></span><span class="brand-name">Elif Grillstube</span></div>
      <ul class="nav"><li>HOME</li><li>ELIF GRILLSTUBE</li><li class="is-active">CATERING</li><li>LIEFERSERVICE</li><li>MENU</li></ul>
      <div class="contact"><svg><use href="#ico-phone"/></svg><p>Lieferservice &amp;<br>Catering:<span class="nums" style="display:block">02302 48120<br>01577 9921365</span></p></div>
      <div class="social"><span class="circle"></span><svg><use href="#ico-mail"/></svg></div>
    </aside>
    <div class="photo ph-pide" role="img" aria-label="Foto: Pide mit Peperoni und Gewürzen" style="left:78px;top:10px;width:170px;height:302px"></div>
    <h1 class="hero-title" style="left:86px;top:34px;font-size:19px">Geschmack<br>&amp;<br>Qualität in<br>Tradition.<span class="underline"></span>Über 20<br>Jahre.</h1>
    <div class="rail"><span class="label">home</span><div class="dots" style="top:130px"><i></i><i></i><i></i><i></i></div><span class="scroll">scroll down</span><span class="arrow"></span></div>
  </div>
  <div class="screen mob">
    <header class="mob-head"><div class="brand"><span class="brand-dot"></span><span class="brand-name">Elif Grillstube</span></div><div class="burger"><i></i><i></i><i></i></div></header>
    <span class="mob-label">home</span>
    <div class="photo ph-pide" role="img" aria-label="Foto: Pide mit Peperoni" style="top:48px;height:170px"></div>
    <h1 class="hero-title" style="top:72px">Geschmack<br>&amp;<br>Qualität in<br>Tradition.<br><br>Über 20<br>Jahre.</h1>
    <footer class="mob-foot"><svg><use href="#ico-phone"/></svg><span>Lieferservice &amp;<br>Catering:</span><span>02302 48120<br>01577 9921365</span><span class="sp"></span><span class="circle"></span><svg><use href="#ico-mail"/></svg></footer>
  </div>
</section>

<!-- ============ ELIF GRILLSTUBE ============ -->
<section class="row" style="top:460px">
  <div class="screen desk">
    <aside class="sidebar">
      <div class="brand"><span class="brand-dot"></span><span class="brand-name">Elif Grillstube</span></div>
      <ul class="nav"><li>HOME</li><li>ELIF GRILLSTUBE</li><li class="is-active">CATERING</li><li>LIEFERSERVICE</li><li>MENU</li></ul>
      <div class="contact"><svg><use href="#ico-phone"/></svg><p>Lieferservice &amp;<br>Catering:<span class="nums" style="display:block">02302 48120<br>01577 9921365</span></p></div>
      <div class="social"><span class="circle"></span><svg><use href="#ico-mail"/></svg></div>
    </aside>
    <div class="photo ph-interior" role="img" aria-label="Foto: Innenraum des Restaurants mit grüner Beleuchtung" style="left:96px;top:10px;width:480px;height:156px"></div>
    <h1 class="hero-title" style="left:124px;top:38px;font-size:21px">Ein Familienbetrieb<br>in zweiter Generation.</h1>
    <div class="body" style="position:absolute;left:114px;top:184px;width:182px">
      <p>Die Elif Grillstube ist ein Familienbetrieb in zweiter Generation und seit 1992 in Hagenfeld tätig. In über 20 Jahren haben wir viele Stammkunden gewinnen können. Aus den Mitteilungen und Feedbacks unserer Kunden erfahren wir, dass so manche gerne einen weiteren Weg kommen (ca. 60 km - nach unseren Erfahrungen), um unsere Köstlichkeiten zu verspeisen. "Wann machen Sie endlich eine Filiale in unserer Nähe auf?" werden wir gefragt, was uns natürlich sehr schmeichelt.</p>
      <p>Dieses Feedback gab uns unter Anderem den Anstoß, das alte Kebaphaus neu zu errichten. Seit Anfang 2016 sind wir in dem Neubau, unter der Hausnummer 27 zu finden. Dort finden unsere Gäste ein größeres und modernes Haus für sich und ihre Lieben.</p>
    </div>
    <span style="position:absolute;left:320px;top:186px;width:2px;height:32px;background:var(--green)"></span>
    <div class="photo map" role="img" aria-label="Karte mit Standort der Grillstube" style="left:342px;top:184px;width:216px;height:98px"></div>
    <p class="body" style="position:absolute;left:342px;top:294px;font-size:7px">Elif Grillstube - Lindenweg 27 - 58100 Hagenfeld</p>
    <p class="body" style="position:absolute;left:342px;top:308px;font-size:7px"><strong>Öffnungszeiten:</strong> Mo-So: von 7.00 bis 23.00</p>
    <div class="rail"><span class="label">elif grillstube</span><span class="scroll">scroll down</span><span class="arrow"></span></div>
  </div>
  <div class="screen tab">
    <aside class="sidebar">
      <div class="brand"><span class="brand-dot"></span><span class="brand-name">Elif Grillstube</span></div>
      <ul class="nav"><li>HOME</li><li>ELIF GRILLSTUBE</li><li class="is-active">CATERING</li><li>LIEFERSERVICE</li><li>MENU</li></ul>
      <div class="contact"><svg><use href="#ico-phone"/></svg><p>Lieferservice &amp;<br>Catering:<span class="nums" style="display:block">02302 48120<br>01577 9921365</span></p></div>
      <div class="social"><span class="circle"></span><svg><use href="#ico-mail"/></svg></div>
    </aside>
    <div class="photo ph-interior" role="img" aria-label="Foto: Innenraum des Restaurants" style="left:78px;top:10px;width:170px;height:144px"></div>
    <h1 class="hero-title" style="left:86px;top:14px;font-size:17px">Ein Familien-<br>betrieb<br>in zweiter<br>Generation.</h1>
    <div class="body" style="position:absolute;left:82px;top:160px;width:162px;font-size:6px">
      <p>Die Elif Grillstube ist ein Familienbetrieb in zweiter Generation und seit 1992 in Hagenfeld tätig. In über 20 Jahren haben wir viele Stammkunden gewinnen können. Aus den Mitteilungen und Feedbacks unserer Kunden erfahren wir, dass so manche gerne einen weiteren Weg kommen (ca. 60 km - nach unseren Erfahrungen), um unsere Köstlichkeiten zu verspeisen. "Wann machen Sie endlich eine Filiale in unserer Nähe auf?" werden wir gefragt, was uns natürlich sehr schmeichelt.</p>
      <p>Dieses Feedback gab uns unter Anderem den Anstoß, das alte Kebaphaus neu zu errichten. Seit Anfang 2016 sind wir in dem Neubau, unter der Hausnummer 27 zu finden. Dort finden unsere Gäste ein größeres und modernes Haus für sich und ihre Lieben.</p>
    </div>
    <div class="photo map" role="img" aria-label="Karte mit Standort" style="left:82px;top:298px;width:162px;height:16px"></div>
    <div class="rail"><span class="label">elif grillstube</span><span class="scroll">scroll down</span><span class="arrow"></span></div>
  </div>
  <div class="screen mob">
    <header class="mob-head"><div class="brand"><span class="brand-dot"></span><span class="brand-name">Elif Grillstube</span></div><div class="burger"><i></i><i></i><i></i></div></header>
    <span class="mob-label">elif grillstube</span>
    <div class="photo ph-interior" role="img" aria-label="Foto: Innenraum des Restaurants" style="top:48px;height:84px"></div>
    <h1 class="hero-title" style="top:56px;font-size:9px">Ein Familien-<br>betrieb<br>in zweiter<br>Generation.</h1>
    <div class="body" style="position:absolute;left:8px;right:8px;top:138px">
      <p>Die Elif Grillstube ist ein Familienbetrieb in zweiter Generation und seit 1992 in Hagenfeld tätig. Viele Stammkunden kommen gerne einen weiteren Weg, um unsere Köstlichkeiten zu genießen.</p>
      <p>Seit Anfang 2016 finden Sie uns im Neubau unter der Hausnummer 27. Dort erwartet unsere Gäste ein größeres und modernes Haus.</p>
    </div>
    <footer class="mob-foot"><svg><use href="#ico-phone"/></svg><span>Lieferservice &amp;<br>Catering:</span><span>02302 48120<br>01577 9921365</span><span class="sp"></span><span class="circle"></span><svg><use href="#ico-mail"/></svg></footer>
  </div>
</section>

<!-- ============ CATERING ============ -->
<section class="row" style="top:890px">
  <div class="screen desk">
    <aside class="sidebar">
      <div class="brand"><span class="brand-dot"></span><span class="brand-name">Elif Grillstube</span></div>
      <ul class="nav"><li>HOME</li><li>ELIF GRILLSTUBE</li><li class="is-active">CATERING</li><li>LIEFERSERVICE</li><li>MENU</li></ul>
      <div class="contact"><svg><use href="#ico-phone"/></svg><p>Lieferservice &amp;<br>Catering:<span class="nums" style="display:block">02302 48120<br>01577 9921365</span></p></div>
      <div class="social"><span class="circle"></span><svg><use href="#ico-mail"/></svg></div>
    </aside>
    <div style="position:absolute;left:122px;top:24px;width:196px">
      <h2 class="sect" style="font-size:21px"><em>Elif</em><br>Catering</h2>
      <span class="underline" style="margin:12px 0 20px"></span>
      <div class="body">
        <p>Ob Firmenfeste, Geburtstage oder sonstige Events - Elif Grillstube stellt ihnen ein individuelles Catering Angebot zusammen.</p>
        <p>Ihre Wünsche als Kunde stehen dabei immer im Vordergrund. Buchen Sie ihr Catering vor Ort oder rufen Sie uns an!</p>
        <p><strong>Sie benötigen Hilfe bei der Planung?</strong><br>Unser Team hilft Ihnen gerne weiter.</p>
      </div>
    </div>
    <div class="photo ph-kebab" role="img" aria-label="Foto: Grillspieße auf Holzbrett mit Salat" style="left:338px;top:10px;width:238px;height:318px"></div>
    <div class="rail"><span class="label">catering</span><span class="scroll">scroll down</span><span class="arrow"></span></div>
  </div>
  <div class="screen tab">
    <aside class="sidebar">
      <div class="brand"><span class="brand-dot"></span><span class="brand-name">Elif Grillstube</span></div>
      <ul class="nav"><li>HOME</li><li>ELIF GRILLSTUBE</li><li class="is-active">CATERING</li><li>LIEFERSERVICE</li><li>MENU</li></ul>
      <div class="contact"><svg><use href="#ico-phone"/></svg><p>Lieferservice &amp;<br>Catering:<span class="nums" style="display:block">02302 48120<br>01577 9921365</span></p></div>
      <div class="social"><span class="circle"></span><svg><use href="#ico-mail"/></svg></div>
    </aside>
    <div class="photo ph-kebab" role="img" aria-label="Foto: Grillspieße auf Holzbrett" style="left:78px;top:10px;width:170px;height:150px"></div>
    <div style="position:absolute;left:84px;top:166px;width:160px">
      <h2 class="sect" style="font-size:19px"><em>Elif</em><br>Catering</h2>
      <span class="underline"></span>
      <div class="body" style="font-size:6.4px">
        <p>Ob Firmenfeste, Geburtstage oder sonstige Events - Elif Grillstube stellt ihnen ein individuelles Catering Angebot zusammen.</p>
        <p>Ihre Wünsche als Kunde stehen dabei immer im Vordergrund. Buchen Sie ihr Catering vor Ort oder rufen Sie uns an!</p>
        <p><strong>Sie benötigen Hilfe bei der Planung?</strong><br>Unser Team hilft Ihnen gerne weiter.</p>
      </div>
    </div>
    <div class="rail"><span class="label">catering</span><span class="scroll">scroll down</span><span class="arrow"></span></div>
  </div>
  <div class="screen mob">
    <header class="mob-head"><div class="brand"><span class="brand-dot"></span><span class="brand-name">Elif Grillstube</span></div><div class="burger"><i></i><i></i><i></i></div></header>
    <span class="mob-label">catering</span>
    <div class="photo ph-kebab" role="img" aria-label="Foto: Grillspieße" style="top:48px;height:80px"></div>
    <h2 class="sect" style="position:absolute;left:10px;top:134px;font-size:8px"><em>Elif</em> Catering</h2>
    <span class="underline" style="position:absolute;left:10px;top:142px;width:14px;height:1px"></span>
    <div class="body" style="position:absolute;left:10px;right:10px;top:154px">
      <p>Ob Firmenfeste oder Geburtstage - wir stellen ihnen ein individuelles Catering Angebot zusammen.</p>
      <p>Buchen Sie vor Ort oder rufen Sie uns an!</p>
      <p><strong>Hilfe bei der Planung?</strong><br>Unser Team hilft gerne.</p>
    </div>
    <footer class="mob-foot"><svg><use href="#ico-phone"/></svg><span>Lieferservice &amp;<br>Catering:</span><span>02302 48120<br>01577 9921365</span><span class="sp"></span><span class="circle"></span><svg><use href="#ico-mail"/></svg></footer>
  </div>
</section>

<!-- ============ LIEFERSERVICE ============ -->
<section class="row" style="top:1320px">
  <div class="screen desk">
    <aside class="sidebar">
      <div class="brand"><span class="brand-dot"></span><span class="brand-name">Elif Grillstube</span></div>
      <ul class="nav"><li>HOME</li><li>ELIF GRILLSTUBE</li><li class="is-active">CATERING</li><li>LIEFERSERVICE</li><li>MENU</li></ul>
      <div class="contact"><svg><use href="#ico-phone"/></svg><p>Lieferservice &amp;<br>Catering:<span class="nums" style="display:block">02302 48120<br>01577 9921365</span></p></div>
      <div class="social"><span class="circle"></span><svg><use href="#ico-mail"/></svg></div>
    </aside>
    <div class="photo ph-baklava" role="img" aria-label="Foto: Baklava mit Pistazien auf dunklem Tisch" style="left:96px;top:10px;width:240px;height:318px"></div>
    <div style="position:absolute;left:368px;top:26px;width:186px">
      <h2 class="sect" style="font-size:21px">Lieferservice</h2>
      <span class="underline" style="margin:12px 0 22px"></span>
      <div class="body">
        <p>Wir liefern alle Köstlichkeiten auch ausser Haus. Ein Anruf genügt.</p>
        <p>Aus dem umfangreichen Speisenangebot können Sie sich Ihre Gerichte zusammenstellen und telefonisch bestellen.</p>
      </div>
    </div>
    <div class="rail"><span class="label">lieferservice</span><span class="scroll">scroll down</span><span class="arrow"></span></div>
  </div>
  <div class="screen tab">
    <aside class="sidebar">
      <div class="brand"><span class="brand-dot"></span><span class="brand-name">Elif Grillstube</span></div>
      <ul class="nav"><li>HOME</li><li>ELIF GRILLSTUBE</li><li class="is-active">CATERING</li><li>LIEFERSERVICE</li><li>MENU</li></ul>
      <div class="contact"><svg><use href="#ico-phone"/></svg><p>Lieferservice &amp;<br>Catering:<span class="nums" style="display:block">02302 48120<br>01577 9921365</span></p></div>
      <div class="social"><span class="circle"></span><svg><use href="#ico-mail"/></svg></div>
    </aside>
    <div class="photo ph-baklava" role="img" aria-label="Foto: Baklava mit Pistazien" style="left:78px;top:10px;width:170px;height:150px"></div>
    <div style="position:absolute;left:84px;top:176px;width:160px">
      <h2 class="sect" style="font-size:19px">Lieferservice</h2>
      <span class="underline"></span>
      <div class="body" style="font-size:6.4px">
        <p>Wir liefern alle Köstlichkeiten auch ausser Haus. Ein Anruf genügt.</p>
        <p>Aus dem umfangreichen Speisenangebot können Sie sich Ihre Gerichte zusammenstellen und telefonisch bestellen.</p>
      </div>
    </div>
    <div class="rail"><span class="label">lieferservice</span><span class="scroll">scroll down</span><span class="arrow"></span></div>
  </div>
  <div class="screen mob">
    <header class="mob-head"><div class="brand"><span class="brand-dot"></span><span class="brand-name">Elif Grillstube</span></div><div class="burger"><i></i><i></i><i></i></div></header>
    <span class="mob-label">lieferservice</span>
    <div class="photo ph-baklava" role="img" aria-label="Foto: Baklava" style="top:48px;height:80px"></div>
    <h2 class="sect" style="position:absolute;left:10px;top:134px;font-size:8px">Lieferservice</h2>
    <span class="underline" style="position:absolute;left:10px;top:142px;width:14px;height:1px"></span>
    <div class="body" style="position:absolute;left:10px;right:10px;top:154px">
      <p>Wir liefern alle Köstlichkeiten auch ausser Haus. Ein Anruf genügt.</p>
      <p>Stellen Sie Ihre Gerichte zusammen und bestellen Sie telefonisch.</p>
    </div>
    <footer class="mob-foot"><svg><use href="#ico-phone"/></svg><span>Lieferservice &amp;<br>Catering:</span><span>02302 48120<br>01577 9921365</span><span class="sp"></span><span class="circle"></span><svg><use href="#ico-mail"/></svg></footer>
  </div>
</section>

<!-- ============ MENU ============ -->
<section class="row" style="top:1750px">
  <div class="screen desk">
    <aside class="sidebar">
      <div class="brand"><span class="brand-dot"></span><span class="brand-name">Elif Grillstube</span></div>
      <ul class="nav"><li>HOME</li><li>ELIF GRILLSTUBE</li><li class="is-active">CATERING</li><li>LIEFERSERVICE</li><li>MENU</li></ul>
      <div class="contact"><svg><use href="#ico-phone"/></svg><p>Lieferservice &amp;<br>Catering:<span class="nums" style="display:block">02302 48120<br>01577 9921365</span></p></div>
      <div class="social"><span class="circle"></span><svg><use href="#ico-mail"/></svg></div>
    </aside>
    <div class="photo ph-terrace" role="img" aria-label="Foto: Terrasse mit Tischen und Stühlen" style="left:96px;top:10px;width:480px;height:150px"></div>
    <h1 class="hero-title" style="left:116px;top:40px;font-size:21px">Guten Appetit!</h1>
    <div class="center" style="position:absolute;left:116px;top:172px;width:440px;text-align:center">
      <p class="body" style="text-align:center">Hier haben Sie die Möglichkeit sich von vorne bis hinten bedienen zu lassen. Wir bereiten alles was Sie sich wünschen frisch zu und bringen es entweder an ihren Tisch oder Sie nehmen es einfach mit nach Hause. Ihren individuellen Wünschen sollen keine Grenzen gesetzt sein, denn Ihre Wünsche als Kunde stehen bei uns immer im Vordergrund.</p>
      <span class="underline" style="margin:12px auto"></span>
      <div style="display:flex;justify-content:space-around;margin-bottom:14px"><span class="btn">SPEISEN</span><span class="btn">GETRÄNKE</span></div>
      <p class="body" style="text-align:center"><strong>Ausgewogen und Gesund essen.</strong><br>Seit 1992 bieten wir unseren Gästen Frische und Geschmack in höchster Qualität.<br>Das Geheimnis ist sehr einfach:<br>Wir sind gerne für Sie da!<br>Ihr Elif Grillstube Team</p>
    </div>
    <div class="rail"><span class="label">menu</span><span class="scroll">scroll down</span><span class="arrow"></span></div>
  </div>
  <div class="screen tab">
    <aside class="sidebar">
      <div class="brand"><span class="brand-dot"></span><span class="brand-name">Elif Grillstube</span></div>
      <ul class="nav"><li>HOME</li><li>ELIF GRILLSTUBE</li><li class="is-active">CATERING</li><li>LIEFERSERVICE</li><li>MENU</li></ul>
      <div class="contact"><svg><use href="#ico-phone"/></svg><p>Lieferservice &amp;<br>Catering:<span class="nums" style="display:block">02302 48120<br>01577 9921365</span></p></div>
      <div class="social"><span class="circle"></span><svg><use href="#ico-mail"/></svg></div>
    </aside>
    <div class="photo ph-terrace" role="img" aria-label="Foto: Terrasse mit Tischen" style="left:78px;top:10px;width:170px;height:150px"></div>
    <h1 class="hero-title" style="left:92px;top:40px;font-size:19px">Guten<br>Appetit!</h1>
    <div class="center" style="position:absolute;left:84px;top:168px;width:160px;text-align:center">
      <p class="body" style="text-align:center;font-size:6.2px">Hier haben Sie die Möglichkeit sich von vorne bis hinten bedienen zu lassen. Wir bereiten alles was Sie sich wünschen frisch zu und bringen es entweder an ihren Tisch oder Sie nehmen es einfach mit nach Hause. Ihren individuellen Wünschen sollen keine Grenzen gesetzt sein, denn Ihre Wünsche als Kunde stehen bei uns immer im Vordergrund.</p>
      <span class="underline"></span>
      <span class="btn" style="margin:4px 0 12px">SPEISEN</span><br>
      <span class="btn">GETRÄNKE</span>
    </div>
    <div class="rail"><span class="label">menu</span><span class="scroll">scroll down</span><span class="arrow"></span></div>
  </div>
  <div class="screen mob">
    <header class="mob-head"><div class="brand"><span class="brand-dot"></span><span class="brand-name">Elif Grillstube</span></div><div class="burger"><i></i><i></i><i></i></div></header>
    <span class="mob-label">menu</span>
    <div class="photo ph-terrace" role="img" aria-label="Foto: Terrasse" style="top:48px;height:80px"></div>
    <h1 class="hero-title" style="top:62px;font-size:10px">Guten<br>Appetit!</h1>
    <div class="center" style="position:absolute;left:10px;right:10px;top:134px;text-align:center">
      <p class="body" style="text-align:center">Wir bereiten alles frisch zu und bringen es an Ihren Tisch oder Sie nehmen es mit nach Hause. Ihre Wünsche stehen bei uns immer im Vordergrund.</p>
      <span class="underline" style="width:14px;height:1px;margin:5px auto"></span>
      <span class="btn" style="font-size:4px;padding:1px 10px;margin-bottom:5px">SPEISEN</span><br>
      <span class="btn" style="font-size:4px;padding:1px 8px">GETRÄNKE</span>
    </div>
    <footer class="mob-foot"><svg><use href="#ico-phone"/></svg><span>Lieferservice &amp;<br>Catering:</span><span>02302 48120<br>01577 9921365</span><span class="sp"></span><span class="circle"></span><svg><use href="#ico-mail"/></svg></footer>
  </div>
</section>

</body>
</html>
```